BOLD & MINIMALIST DESIGN NEEDED

We want a very bold but minimalistic business card design that is impactful and utilizes both sides of the business card. Our current logo is included for your use.

We want bold fonts and good use of negative space. We don't want the logo to overpower the design.

Target Market(s)

Professionals who are building new commercial buildings.

Industry/Entity Type

Construction

Contact Information for Business Card

Name, Title, email, office phone, cell phone, website

Font styles to use
Serif
Sans Serif

Requirements
Must have
• Bold design!

```html
<!DOCTYPE html>
<html lang="en">
<head>
<meta charset="utf-8">
<title>Summitcrest Business Card</title>
<link href="https://fonts.googleapis.com/css2?family=Poppins:wght@400;500;800&family=Barlow+Semi+Condensed:wght@400&display=swap" rel="stylesheet">
<style>
  :root {
    --page: #d4d4d4;
    --paper: #ffffff;
    --ink: #1a1a1a;
    --night: #141414;
    --night-soft: #262626;
    --lime: #6cbd26;
    --lime-bright: #7dcc2e;
    --muted: #3a3a3a;
  }
  * { margin: 0; padding: 0; box-sizing: border-box; }
  html, body { width: 1200px; height: 1200px; overflow: hidden; }
  body {
    background: var(--page);
    font-family: "Poppins", sans-serif;
    position: relative;
  }
  .card {
    position: absolute;
    left: 257px;
    width: 686px;
    height: 392px;
    box-shadow: 0 18px 30px rgba(0,0,0,0.22);
  }
  .card-front { top: 165px; background: var(--paper); }
  .card-back {
    top: 653px;
    background: linear-gradient(135deg, var(--night) 40%, var(--night-soft) 100%);
  }
  .brand {
    position: absolute;
    display: flex;
    align-items: center;
    gap: 10px;
    font-weight: 800;
    letter-spacing: 0.5px;
    text-transform: uppercase;
  }
  .brand-mark { width: 18px; height: 18px; background: var(--lime); }
  .card-front .brand {
    right: 36px;
    top: 132px;
    font-size: 34px;
    color: var(--ink);
  }
  .card-back .brand {
    left: 0; right: 0;
    top: 166px;
    justify-content: center;
    font-size: 48px;
    color: #ffffff;
  }
  .card-back .brand-mark { width: 24px; height: 24px; }
  .person-name {
    position: absolute;
    left: 32px; top: 188px;
    font-size: 24px;
    font-weight: 400;
    color: var(--lime);
    letter-spacing: 0.3px;
  }
  .person-title {
    position: absolute;
    left: 32px; top: 223px;
    font-size: 16px;
    font-weight: 500;
    color: var(--ink);
  }
  .divider {
    position: absolute;
    left: 32px; top: 252px;
    width: 624px; height: 1px;
    background: var(--ink);
  }
  .contact-list {
    position: absolute;
    left: 34px; top: 280px;
    list-style: none;
    font-size: 15.5px;
    color: var(--muted);
    letter-spacing: 0.6px;
    line-height: 20px;
  }
  .contact-list li { display: flex; align-items: center; gap: 12px; }
  .contact-list svg { width: 14px; height: 14px; }
  .address {
    position: absolute;
    right: 30px; top: 281px;
    text-align: right;
    font-family: "Barlow Semi Condensed", sans-serif;
    font-size: 17px;
    line-height: 21px;
    color: var(--muted);
    letter-spacing: 0.4px;
  }
  .footer-bands { position: absolute; left: 0; bottom: 0; width: 686px; height: 46px; }
  .website {
    position: absolute;
    left: 430px; bottom: 10px;
    font-size: 15px;
    letter-spacing: 3.6px;
    color: var(--lime-bright);
  }
</style>
</head>
<body>
  <section class="card card-front">
    <div class="brand"><span class="brand-mark"></span>Summitcrest</div>
    <h1 class="person-name">DANIEL HARPER</h1>
    <p class="person-title">PRESIDENT</p>
    <div class="divider"></div>
    <ul class="contact-list">
      <li>
        <svg viewBox="0 0 24 24"><path fill="#6cbd26" d="M6.6 10.8a15.1 15.1 0 0 0 6.6 6.6l2.2-2.2c.3-.3.7-.4 1-.2 1.1.4 2.3.6 3.6.6.6 0 1 .4 1 1V20c0 .6-.4 1-1 1A17 17 0 0 1 3 4c0-.6.4-1 1-1h3.5c.6 0 1 .4 1 1 0 1.3.2 2.5.6 3.6.1.3 0 .7-.2 1z"/></svg>
        555-014-2287
      </li>
      <li>
        <svg viewBox="0 0 24 24"><rect x="2" y="5" width="20" height="14" fill="#6cbd26"/><path d="M2 5l10 8 10-8" fill="none" stroke="#ffffff" stroke-width="1.6"/></svg>
        INFO@SUMMITCREST.COM
      </li>
    </ul>
    <address class="address" style="font-style:normal">418 BIRCHWOOD LANE<br>FAIRBANKS, ALASKA 99701</address>
    <svg class="footer-bands" viewBox="0 0 686 46" preserveAspectRatio="none">
      <polygon points="0,16 400,16 386,30 0,30" fill="#6cbd26"/>
      <polygon points="421,0 686,0 686,46 0,46 0,33 388,33" fill="#141414"/>
    </svg>
    <span class="website">WWW.SUMMITCREST.COM</span>
  </section>

  <section class="card card-back">
    <div class="brand"><span class="brand-mark"></span>Summitcrest</div>
  </section>
</body>
</html>
```